Property Development Business Cards

I need a business card design for Blue Harbour Developments Pty Ltd. We are a property development company in Australia and our name defines the five values that we adhere to, being Profitable, Partnerships, Quality Developments, Eco Friendly and Enduring Design.

I have attached the current logo that I use, it is just five yellow circles connected to a single cricle in the middle.

Target Market(s)

Our Target audience is real estate agents, owners of properties, builders and other trades

Industry/Entity Type

Business

Requirements
Must have
• Want to have two sides to the card, one with details and one to just highlight the company

```html
<!DOCTYPE html>
<html lang="en">
<head>
<meta charset="utf-8">
<title>Blue Harbour Developments Pty Ltd — Business Card</title>
<link rel="stylesheet" href="https://fonts.googleapis.com/css2?family=Arimo:wght@400;700&display=swap">
<style>
  :root {
    --card-white: #ffffff;
    --brand-blue: #0a80f0;
    --divider-grey: #cccccc;
    --band-yellow: #ffe600;
    --band-orange: #ff9a00;
    --mark-yellow: #ffc800;
    --text-dark: #111111;
  }
  html, body {
    margin: 0;
    padding: 0;
    width: 1200px;
    height: 777px;
    overflow: hidden;
    background: var(--card-white);
  }
  .card {
    position: relative;
    width: 1200px;
    height: 777px;
    background: var(--card-white);
    font-family: "Arimo", Arial, sans-serif;
  }
  .card-side {
    position: absolute;
    left: 0;
    width: 100%;
    margin: 0;
  }
  .card-side--brand {
    top: 0;
    height: 494px;
    background: var(--card-white);
  }
  .brand-mark {
    position: absolute;
    left: 563px;
    top: 174px;
    width: 74px;
    height: 74px;
  }
  .company-name {
    position: absolute;
    left: 0;
    right: 0;
    top: 357px;
    margin: 0;
    text-align: center;
    font-weight: 700;
    font-size: 41.5px;
    line-height: 50px;
    color: var(--brand-blue);
    white-space: nowrap;
  }
  .divider {
    position: absolute;
    left: 0;
    top: 494px;
    width: 100%;
    height: 12px;
    background: var(--divider-grey);
  }
  .card-side--details {
    top: 506px;
    height: 271px;
    background: linear-gradient(to bottom, var(--band-yellow) 0%, var(--band-orange) 52%, var(--band-orange) 100%);
  }
  .contact-details {
    position: absolute;
    left: 74px;
    top: 50px;
    margin: 0;
    font-style: normal;
    font-weight: 400;
    font-size: 31px;
    line-height: 41.5px;
    color: var(--text-dark);
    white-space: nowrap;
  }
</style>
</head>
<body>
  <main class="card">
    <section class="card-side card-side--brand" aria-label="Company side">
      <svg class="brand-mark" viewBox="0 0 74 74" aria-hidden="true">
        <circle cx="37" cy="37" r="37" fill="var(--mark-yellow)"/>
      </svg>
      <h1 class="company-name">Blue Harbour Developments Pty Ltd</h1>
    </section>
    <div class="divider"></div>
    <section class="card-side card-side--details" aria-label="Details side">
      <address class="contact-details">
        PO Box 728<br>
        Harbourview, ACT 2990<br>
        info@BlueHarbourDevelopments.com.au<br>
        www.blueharbourdevelopments.com.au
      </address>
    </section>
  </main>
</body>
</html>
```